Re-Design of Business Card for Marine Sales People

We are looking to Re-design our business cards to look like they are in the 21st century. We are a full service marina and sell a lot of new/used boats. May want a spot on the card for our 3 main brands we sell. A picture spot of the sales man would be nice, but not necessarily.

```html
<!DOCTYPE html>
<html lang="en">
<head>
<meta charset="utf-8">
<title>Lakeport Marine – Business Card</title>
<link href="https://fonts.googleapis.com/css2?family=Lato:wght@400;700;900&display=swap" rel="stylesheet">
<style>
  :root {
    --backdrop: #2b2a2a;
    --navy: #1c3760;
    --navy-light: #27466f;
    --sky: #1c9ad8;
    --ink: #2c3440;
    --paper: #ffffff;
    --rule: #b9bec6;
  }
  * { box-sizing: border-box; margin: 0; padding: 0; }
  html, body {
    width: 1200px; height: 939px; overflow: hidden;
    background: var(--backdrop);
    font-family: "Lato", sans-serif;
  }
  .canvas {
    position: relative; width: 1200px; height: 939px;
  }
  .card {
    position: absolute; left: 290px; width: 620px; height: 354px;
    border-radius: 22px; overflow: hidden;
  }
  .card--front {
    top: 86px;
    background: linear-gradient(135deg, var(--navy) 0%, var(--navy-light) 100%);
    display: flex; align-items: center; justify-content: center;
  }
  .card--back {
    top: 500px; background: var(--paper);
    display: flex;
  }
  .brand {
    display: flex; align-items: center; gap: 14px;
    font-weight: 900; letter-spacing: 3px; text-transform: uppercase;
  }
  .brand__dot {
    width: 16px; height: 16px; border-radius: 50%; background: var(--sky);
  }
  .card--front .brand { font-size: 44px; color: var(--paper); }
  .card--back .brand { font-size: 25px; color: var(--navy); letter-spacing: 2px; }
  .card--back .brand__dot { width: 11px; height: 11px; }
  .back__logo {
    width: 52%; display: flex; align-items: center; justify-content: center;
  }
  .back__divider {
    width: 1px; margin: 40px 0; background: var(--rule);
  }
  .back__info {
    flex: 1; padding: 44px 30px 0 30px;
  }
  .person__name {
    font-weight: 900; font-size: 29px; color: var(--navy); line-height: 1;
  }
  .person__role {
    font-size: 18px; color: var(--sky); margin-top: 5px; margin-bottom: 18px;
  }
  .contact { list-style: none; font-size: 14.5px; color: var(--ink); }
  .contact li {
    display: flex; align-items: flex-start; gap: 12px; line-height: 1.35;
    margin-bottom: 5px;
  }
  .contact li.contact__address { margin-bottom: 14px; }
  .contact svg { width: 13px; height: 13px; flex: none; margin-top: 3px; fill: var(--sky); }
</style>
</head>
<body>
<main class="canvas">

  <section class="card card--front" aria-label="Card front">
    <div class="brand"><span class="brand__dot"></span>Lakeport Marine</div>
  </section>

  <section class="card card--back" aria-label="Card back">
    <div class="back__logo">
      <div class="brand"><span class="brand__dot"></span>Lakeport Marine</div>
    </div>
    <div class="back__divider"></div>
    <div class="back__info">
      <h1 class="person__name">DANIEL HART</h1>
      <p class="person__role">Founder &amp; CEO</p>
      <ul class="contact">
        <li class="contact__address">
          <svg viewBox="0 0 12 16"><path d="M6 0a6 6 0 0 0-6 6c0 4.5 6 10 6 10s6-5.5 6-10a6 6 0 0 0-6-6zm0 8.5A2.5 2.5 0 1 1 6 3.5a2.5 2.5 0 0 1 0 5z"/></svg>
          <span>Address, City, State<br>Country, Zip Code 01235</span>
        </li>
        <li>
          <svg viewBox="0 0 16 16"><path d="M3.6 1l2.5 3-1.4 1.8a9 9 0 0 0 5.5 5.5l1.8-1.4 3 2.5-1.3 2.6C8 15 1 8 1 2.3z"/></svg>
          <span>(123) 456-7890</span>
        </li>
        <li>
          <svg viewBox="0 0 12 16"><path d="M2 0h8a1.5 1.5 0 0 1 1.5 1.5v13A1.5 1.5 0 0 1 10 16H2A1.5 1.5 0 0 1 .5 14.5v-13A1.5 1.5 0 0 1 2 0zm0 2v10h8V2zm4 11a1 1 0 1 0 0 2 1 1 0 0 0 0-2z"/></svg>
          <span>(231) 456-7890</span>
        </li>
        <li>
          <svg viewBox="0 0 16 16"><path d="M4 0h8v4H4zM1 5h14v7h-3v4H4v-4H1zm5 6v3h4v-3z"/></svg>
          <span>(312) 456-7890</span>
        </li>
        <li>
          <svg viewBox="0 0 16 12"><path d="M0 0h16v1.5L8 7 0 1.5zm0 3.3l8 5.5 8-5.5V12H0z"/></svg>
          <span>office@mywebsite.com</span>
        </li>
        <li>
          <svg viewBox="0 0 16 16"><path d="M8 0a8 8 0 1 0 0 16A8 8 0 0 0 8 0zm0 2c.8 0 2 1.8 2.3 5H5.7C6 3.8 7.2 2 8 2zM5.7 9h4.6C10 12.2 8.8 14 8 14s-2-1.8-2.3-5z"/></svg>
          <span>www.mywebsite.com</span>
        </li>
      </ul>
    </div>
  </section>

</main>
</body>
</html>
```